Book Cover " FROM GRAVEL TO AMBER"

Looking for a book cover for a novel from Gravel to Amber.
Amber is the characters developed name. The book describes his rough up bringing and how he obtains his greatness and his given name Amber.

```html
<!DOCTYPE html>
<html lang="en">
<head>
<meta charset="utf-8">
<title>From Gravel to Amber — Book Cover</title>
<link rel="stylesheet" href="https://fonts.googleapis.com/css2?family=Cinzel:wght@600;700&family=Montserrat:wght@700&display=swap">
<style>
  :root {
    --backdrop: #ebe3d5;
    --sand-light: #e3c48f;
    --sand-mid: #c9a46a;
    --sand-dark: #8f6e42;
    --water-light: #2f86b8;
    --water-deep: #0f4d7c;
    --title-brown: #4a2c18;
    --title-rust: #7b3618;
    --author-white: #ffffff;
  }
  html, body {
    margin: 0;
    padding: 0;
    width: 1200px;
    height: 1150px;
    overflow: hidden;
    background: var(--backdrop);
  }
  .canvas {
    position: relative;
    width: 1200px;
    height: 1150px;
  }
  .book-cover {
    position: absolute;
    left: 210px;
    top: 75px;
    width: 780px;
    height: 1000px;
    overflow: hidden;
    box-shadow: 0 6px 18px rgba(60, 45, 25, 0.25);
  }
  .cover-photo {
    position: absolute;
    inset: 0;
    background:
      radial-gradient(ellipse 60% 40% at 40% 55%, rgba(255, 236, 190, 0.55), transparent 70%),
      linear-gradient(100deg,
        var(--sand-dark) 0%,
        var(--sand-mid) 18%,
        var(--sand-light) 42%,
        var(--sand-mid) 58%,
        var(--water-light) 72%,
        var(--water-deep) 100%);
  }
  .title {
    position: absolute;
    left: 90px;
    top: 150px;
    width: 520px;
    margin: 0;
    text-align: center;
    font-family: "Cinzel", serif;
    font-weight: 700;
    color: var(--title-brown);
    line-height: 0.95;
  }
  .title-line {
    display: block;
  }
  .title-from,
  .title-to {
    font-size: 58px;
  }
  .title-gravel {
    font-size: 70px;
  }
  .title-name {
    font-size: 150px;
    color: var(--title-rust);
    margin-top: 6px;
  }
  .author {
    position: absolute;
    left: 330px;
    top: 820px;
    margin: 0;
    font-family: "Montserrat", sans-serif;
    font-weight: 700;
    font-size: 42px;
    letter-spacing: 26px;
    color: var(--author-white);
  }
</style>
</head>
<body>
  <main class="canvas">
    <section class="book-cover">
      <div class="cover-photo" role="img" aria-label="Aerial photograph of a sandy beach meeting blue sea water, with a lone man carrying a suitcase walking along the shoreline"></div>
      <h1 class="title">
        <span class="title-line title-from">FROM</span>
        <span class="title-line title-gravel">GRAVEL</span>
        <span class="title-line title-to">TO</span>
        <span class="title-line title-name">AMBER</span>
      </h1>
      <p class="author">AUTHOR</p>
    </section>
  </main>
</body>
</html>
```